Personal Finance Author needs a postcard

Hi there,

I am a Canadian personal finance author and have published a new book called The Wealth Compass.

I teach Millennials how to create a 6-figure portfolio through investing (https://www.dariafelt.com/)

I'm speaking at some conferences so we were going to print some postcards to hand out to attendees with our info and calls-to-action on them.

I am looking for 4x6 (horizontal) postcard (no space needed for shipping label).

Logos, Headshots and Book Cover:
https://files.cloudvaultex.com/folders/8kQpZrT2mWvN4xLbJ7sHdYc3FgA9eUoRi?usp=sharing

Both sides will be full colour. I would like a clean and simple look. Our main sites are www.DariaFelt.com and www.TheWealthCompassBook.com if you want to get a sense of style and design.
I also uploaded a few marketing materials so you can see the existing designs.

Side 1:
Get Instant Access to your Free Resources - main headline

(small bullets underneath)
- The Wealth Compass Checklist
- Financial Worksheets
- Database of Investment Tools

DariaFelt.com/Resources

At the bottom, include "Don't forget to follow Daria Felt on social media:
Linkedin: @dariafelt7
Facebook: @thewealthcompassbook Instagram: @thewealthcompassbook Twitter: @WealthCompassBk"

Side 2:
Headline - Want to work directly with Daria and The Wealth Compass team to help you make your money grow and stay safe?

Work with us to (bullet point list)...
- Hire Daria as a Keynote Speaker
- Teach Financial Literacy Workshops
- Receive Financial Coaching

Want To Learn More About How We Can Help?
DariaFelt.com/Services

Include my contact info:
Daria Felt
Author | Speaker | Investor
daria@thewealthcompassbook.com
416-555-0187

Target Market(s)

Millennials who want to learn how to save and invest their money. I focus on stock market investing, real estate investing and entrepreneurship.

Industry/Entity Type

Financial Service

Font styles to use
Sans Serif

Colors

Designer to choose colors to be used in the design.

Requirements
Must have
• Photo of Daria Felt
• The Wealth Compass logo
• Green, Gold/Yellow to match existing colours
• modern business style postcard

```html
<!DOCTYPE html>
<html lang="en">
<head>
<meta charset="utf-8">
<title>The Wealth Compass — Postcard</title>
<link rel="stylesheet" href="https://fonts.googleapis.com/css2?family=Poppins:wght@500;600&family=Roboto:ital,wght@0,500;1,500&family=Roboto+Condensed:wght@600&family=Lato:wght@400;700&display=swap">
<style>
  :root {
    --green: #0a5a2e;
    --green-bright: #0d7a3a;
    --gold: #d9a21e;
    --gold-text: #e2b019;
    --ink: #1d1d1d;
    --grey-text: #555a5e;
    --paper: #ffffff;
    --stage: #e6e6e6;
    --soft: #ececec;
    --stripe: #dcdcdc;
  }
  * { box-sizing: border-box; margin: 0; padding: 0; }
  html, body { width: 1200px; height: 800px; overflow: hidden; }
  body {
    background: var(--stage);
    position: relative;
    font-family: "Lato", sans-serif;
  }
  .postcard {
    position: absolute;
    top: 212px;
    width: 565px;
    height: 377px;
    background: var(--paper);
    overflow: hidden;
    box-shadow: 0 6px 18px rgba(0,0,0,.18);
  }
  .postcard--front { left: 30px; }
  .postcard--back { left: 605px; }

  /* ---------- Front ---------- */
  .front-backdrop {
    position: absolute; left: 50px; top: 78px; width: 500px; height: 168px;
    background: linear-gradient(90deg, #f3f3f3, #e8e8e8 60%, #f1f1f1);
  }
  .brand-name {
    position: absolute; left: 62px; top: 26px; width: 130px;
    font-family: "Poppins", sans-serif; font-weight: 600;
    font-size: 17px; line-height: 1.05; color: var(--green);
    text-transform: uppercase; letter-spacing: .5px;
  }
  .front-photo {
    position: absolute; left: 310px; top: 18px; width: 240px; height: 228px;
    background: linear-gradient(180deg, #d8d2cc 0%, #2a2d33 55%, #1c1e22 100%);
    border-radius: 4px 4px 0 0;
  }
  .headline {
    position: absolute; left: 40px; top: 104px; width: 262px; z-index: 2;
    font-family: "Poppins", sans-serif; font-weight: 600;
    font-size: 24px; line-height: 1.02; color: var(--green-bright);
    text-align: center;
  }
  .headline .accent { color: var(--gold-text); display: block; }
  .call-us {
    position: absolute; left: 92px; top: 200px;
    font-family: "Roboto", sans-serif; font-weight: 500; font-size: 11px; color: var(--ink);
  }
  .call-us b { color: var(--green-bright); font-style: italic; }
  .front-band {
    position: absolute; left: 0; top: 246px; width: 100%; height: 20px;
    background: var(--green-bright);
  }
  .resource-list {
    position: absolute; left: 36px; top: 276px; list-style: none;
    font-family: "Roboto", sans-serif; font-style: italic; font-weight: 500;
    font-size: 13px; line-height: 21px; color: var(--ink);
  }
  .resource-url {
    position: absolute; left: 32px; top: 342px;
    font-family: "Roboto", sans-serif; font-weight: 500; font-size: 13px; color: var(--ink);
  }
  .divider {
    position: absolute; left: 282px; top: 280px; width: 3px; height: 76px;
    background: var(--gold);
  }
  .social {
    position: absolute; left: 314px; top: 278px;
    font-family: "Lato", sans-serif; color: var(--ink);
  }
  .social-intro { font-weight: 700; font-size: 10.5px; line-height: 13px; margin-bottom: 6px; }
  .social-list { list-style: none; font-size: 9.5px; font-weight: 700; line-height: 14px; }
  .social-list li { display: flex; align-items: center; gap: 4px; }
  .social-list li::before {
    content: ""; width: 9px; height: 9px; border-radius: 50%; background: var(--green-bright);
  }

  /* ---------- Back ---------- */
  .offer-panel {
    position: absolute; left: 0; top: 0; width: 268px; height: 224px;
    background: var(--green); color: #fff; padding: 22px 0 0 22px;
  }
  .offer-title {
    font-family: "Lato", sans-serif; font-size: 15px; line-height: 22px;
    text-transform: uppercase; font-weight: 400;
  }
  .offer-title strong { font-weight: 700; }
  .offer-intro { margin-top: 12px; margin-left: 2px; font-size: 12px; line-height: 16px; }
  .offer-list { list-style: none; margin-left: 2px; font-size: 12px; line-height: 16px; }
  .cta-band {
    position: absolute; left: 0; top: 224px; width: 276px; height: 56px;
    background: var(--gold); padding: 12px 0 0 24px;
    font-family: "Roboto Condensed", sans-serif; font-weight: 600;
    font-size: 11px; line-height: 16px; color: #fff;
  }
  .contact-block {
    position: absolute; left: 0; top: 280px; width: 280px; height: 97px;
    background: repeating-linear-gradient(135deg, var(--soft) 0 3px, var(--stripe) 3px 4px);
    padding: 11px 0 0 24px; font-style: normal;
    font-size: 11.5px; line-height: 15px; color: var(--grey-text);
  }
  .back-photo {
    position: absolute; left: 300px; top: 12px; width: 250px; height: 365px;
    background: linear-gradient(180deg, #d9d2ca 0%, #26282d 40%, #1b1d21 100%);
    border-radius: 4px 4px 0 0;
  }
</style>
</head>
<body>

<section class="postcard postcard--front" aria-label="Postcard front">
  <div class="front-backdrop"></div>
  <div class="brand-name">The Wealth Compass</div>
  <div class="front-photo" role="img" aria-label="Photo of Daria Felt in a dark blazer holding a calculator and pointing at it"></div>
  <h1 class="headline">Get Instant Access to your <span class="accent">Free Resources</span></h1>
  <p class="call-us"><b>Call us:</b> 416-555-0187</p>
  <div class="front-band"></div>
  <ul class="resource-list">
    <li>- The Wealth Compass Checklist</li>
    <li>- Financial Worksheets</li>
    <li>- Database of Investment Tools</li>
  </ul>
  <p class="resource-url">Visit DariaFelt.com/Resources</p>
  <div class="divider"></div>
  <div class="social">
    <p class="social-intro">Don't forget to follow Daria Felt<br>on social media:</p>
    <ul class="social-list">
      <li>@dariafelt7</li>
      <li>@thewealthcompassbook</li>
      <li>@thewealthcompassbook</li>
      <li>@WealthCompassBk</li>
    </ul>
  </div>
</section>

<section class="postcard postcard--back" aria-label="Postcard back">
  <div class="offer-panel">
    <h2 class="offer-title"><strong>Want to work directly with Daria and The Wealth Compass team to help you</strong> make your money grow and stay safe?</h2>
    <p class="offer-intro">Work with us to</p>
    <ul class="offer-list">
      <li>- Hire Daria as a Keynote Speaker</li>
      <li>- Teach Financial Literacy Workshops</li>
      <li>- Receive Financial Coaching</li>
    </ul>
  </div>
  <div class="cta-band">
    <p>Want To Learn More About How We Can Help?</p>
    <p>DariaFelt.com/Services</p>
  </div>
  <address class="contact-block">
    Daria Felt<br>
    Author | Speaker | Investor<br>
    daria@thewealthcompassbook.com<br>
    416-555-0187
  </address>
  <div class="back-photo" role="img" aria-label="Photo of Daria Felt standing in a dark blazer with hand on hip"></div>
</section>

</body>
</html>
```